KRT Design Business Card

I need to develop a business card for my real estate design and investment company. Something clean, classic and professional with a modern vibe.

Industry/Entity Type

Real Estate

Font styles to use
Serif
Sans Serif

```html
<!DOCTYPE html>
<html lang="en">
<head>
<meta charset="UTF-8">
<title>KRT Design Business Card</title>
<link rel="stylesheet" href="https://fonts.googleapis.com/css2?family=Didact+Gothic&display=swap">
<style>
  :root {
    --canvas-bg: #ecebe8;
    --card-dark: #333333;
    --card-light: #ffffff;
    --ink-light: #f2f2f2;
    --ink-dark: #2a2a2a;
    --ink-muted: #8a8a8a;
    --line-tone-1: #4a4a4a;
    --line-tone-2: #3a3a3a;
    --card-shadow: rgba(0, 0, 0, 0.18);
  }
  * { box-sizing: border-box; margin: 0; padding: 0; }
  html, body {
    width: 1200px;
    height: 900px;
    overflow: hidden;
    background: var(--canvas-bg);
    font-family: "Didact Gothic", "Century Gothic", sans-serif;
  }
  .canvas {
    width: 1200px;
    height: 900px;
    display: flex;
    justify-content: center;
    align-items: center;
    gap: 60px;
  }
  .card {
    width: 300px;
    height: 525px;
    position: relative;
    box-shadow: 0 6px 18px var(--card-shadow);
    overflow: hidden;
  }
  .card--front { background: var(--card-dark); color: var(--ink-light); }
  .card--back { background: var(--card-light); color: var(--ink-dark); }

  .brand {
    position: absolute;
    top: 92px;
    left: 0;
    right: 0;
    text-align: center;
    font-weight: 400;
  }
  .brand__name {
    display: block;
    font-size: 46px;
    letter-spacing: 6px;
    line-height: 1;
  }
  .brand__tagline {
    display: block;
    font-size: 13px;
    letter-spacing: 0.5px;
    margin-top: 8px;
  }
  .card--front .brand__name,
  .card--front .brand__tagline { color: var(--ink-light); }
  .card--back .brand__name,
  .card--back .brand__tagline { color: var(--ink-dark); }

  .building-render {
    position: absolute;
    left: 0;
    right: 0;
    bottom: 0;
    height: 250px;
    background: linear-gradient(160deg, var(--card-dark) 0%, var(--line-tone-1) 55%, var(--line-tone-2) 100%);
  }

  .services {
    position: absolute;
    top: 248px;
    left: 0;
    right: 0;
    text-align: center;
    font-size: 12.5px;
    line-height: 1.35;
    color: var(--ink-muted);
  }
  .services ul { list-style: none; margin-top: 2px; }
  .services li::before { content: "\2022\00a0"; }

  .contact {
    position: absolute;
    top: 372px;
    left: 0;
    right: 0;
    text-align: center;
    font-size: 13px;
    line-height: 1.35;
    color: var(--ink-dark);
  }
</style>
</head>
<body>
  <main class="canvas">
    <section class="card card--front" aria-label="Business card front">
      <div class="brand">
        <span class="brand__name">KRT</span>
        <span class="brand__tagline">Design and Productions</span>
      </div>
      <div class="building-render" role="img" aria-label="Line drawing of a modern two-storey house"></div>
    </section>

    <section class="card card--back" aria-label="Business card back">
      <div class="brand">
        <span class="brand__name">KRT</span>
        <span class="brand__tagline">Design and Productions</span>
      </div>
      <div class="services">
        <p>Brief overview of services<br>or a bullet pointed<br>list could go here:</p>
        <ul>
          <li>First</li>
          <li>Second</li>
          <li>Third</li>
        </ul>
      </div>
      <div class="contact">
        <p>telephone number</p>
        <p>Email address@address.com</p>
        <p>www.krtdesign.com</p>
      </div>
    </section>
  </main>
</body>
</html>
```